New singe page website for our software development company

We need a single webpage that includes information about our company, contact details and a job posting. It should scroll vertically with some cool animations and parallax scrolling effects.

We are a software development consulting company that writes custom software for our customers. The webpage should have graphics and illustrations that illustrate this.

Find our logo attached, it can be modified as needed.

Thanks for all the design. When looking through the various design it's clear to us, that car related images does not look right.

We got to have software design/engineering images instead.

Our unique selling points are:

• Custom software development
• Project Managment
• Industry Services
We want these displayed with some text and icons. The icons should either have the red/brown colour from our logo, or a colour that matches the design

Software

```html
<!DOCTYPE html>
<html lang="en">
<head>
<meta charset="utf-8">
<title>CodeHarbor – Software Consulting</title>
<link rel="stylesheet" href="https://fonts.googleapis.com/css2?family=Open+Sans:wght@400;600;700&display=swap">
<style>
:root{
  --brand:#8a2a12;
  --brand-dark:#6e200d;
  --ink:#333;
  --muted:#8a8a8a;
  --light:#efefef;
  --white:#fff;
  --black:#000;
  --diamond:#c9958a;
  --field:#7a5a45;
}
*{box-sizing:border-box;margin:0;padding:0}
html,body{width:1200px;height:3750px;overflow:hidden}
body{font-family:"Open Sans",Arial,sans-serif;color:var(--ink);position:relative;background:var(--white)}
section,header,footer{position:absolute;left:0;width:1200px}
.abs{position:absolute}

/* header */
.site-header{top:0;height:65px;background:var(--white);border-top:4px solid var(--brand);box-shadow:0 1px 3px rgba(0,0,0,.15);z-index:2}
.brand{left:130px;top:14px;display:flex;align-items:center;gap:8px;font-size:22px;font-weight:700;color:var(--brand)}
.brand-dot{width:12px;height:12px;border-radius:50%;background:var(--brand)}
.main-nav{right:130px;top:22px;display:flex;gap:40px;font-size:14px;font-weight:600;color:#555}
.main-nav .active{color:var(--brand)}

/* hero */
.hero{top:65px;height:585px;background:radial-gradient(ellipse at 55% 60%,#7f8794 0%,#363b44 38%,#121418 78%)}
.hero-caption{left:245px;top:193px;width:635px;height:175px;background:rgba(20,20,20,.82);border-radius:8px;color:var(--white);font-size:26px;line-height:44px;text-align:center;padding-top:42px}
.btn{display:block;background:var(--brand);color:var(--white);font-weight:600;text-align:center;border-radius:8px}
.hero-btn{left:530px;top:405px;width:138px;height:46px;line-height:42px;font-size:17px;border:2px solid #c46a4a}
.hero-arrow{top:262px;width:60px;height:60px}

/* section titles */
.section-title{width:1200px;text-align:center;font-size:32px;color:#333;font-weight:400}
.diamond{left:560px;width:80px;height:80px}

/* about */
.about{top:650px;height:535px;background:var(--light)}
.about-col{width:290px;text-align:center}
.about-col h3{font-size:18px;font-weight:600;color:var(--brand);margin-bottom:16px}
.about-col p{font-size:11px;line-height:19px;color:var(--muted)}
.team-title{width:1200px;text-align:center;top:258px;font-size:17px;color:var(--brand)}
.member{display:flex;gap:18px;width:300px}
.member-photo{width:70px;height:70px;transform:rotate(45deg);margin:15px;background:linear-gradient(135deg,#e3c4ad,#8a6b5a);border:3px solid var(--white);box-shadow:0 1px 4px rgba(0,0,0,.3);flex:none}
.member-info{font-size:10.5px;line-height:17px;color:var(--muted)}
.member-info strong{display:block;color:var(--brand);font-size:12px;font-weight:600;margin-bottom:4px}

/* services */
.services{top:1185px;height:570px;background:var(--black);color:var(--white)}
.services .section-title{color:var(--white)}
.service{display:flex;gap:25px;width:330px}
.service-icon{width:56px;height:56px;border-radius:8px;flex:none;display:flex;align-items:center;justify-content:center}
.service h4{font-size:14px;font-weight:600;margin-bottom:6px;white-space:nowrap}
.service p{font-size:11px;line-height:19px;color:#ccc}

/* works */
.works{top:1755px;height:865px;background:var(--white)}
.work{width:288px;text-align:center}
.work-image{width:288px;height:220px;border:1px solid #ddd}
.work h4{font-size:14px;font-weight:600;color:var(--brand);margin-top:18px}
.work p{font-size:11.5px;color:#666;margin-top:6px}

/* jobs */
.jobs{top:2620px;height:220px;background:linear-gradient(180deg,#8d8478 0%,#5a4e45 55%,#2e2722 100%)}
.jobs h2{width:1200px;top:28px;text-align:center;font-size:38px;font-weight:400;color:var(--white);letter-spacing:1px}
.jobs p{width:1200px;top:82px;text-align:center;font-size:15px;line-height:25px;color:var(--white)}
.jobs-btn{left:515px;top:148px;width:170px;height:40px;line-height:40px;font-size:16px;font-weight:400}

/* tweet */
.tweet{top:2840px;height:315px;background:var(--light)}
.tweet-mark{left:586px;top:42px;width:28px;height:28px;border-radius:50%;background:#2fb6e8}
.tweet-text{left:170px;top:92px;width:860px;font-size:13.5px;line-height:25px;color:#555;text-align:center}
.tweet-quote{left:135px;top:85px;font-size:38px;color:#2fb6e8;font-weight:700;line-height:30px}
.tweet-time{width:1200px;top:152px;text-align:center;font-size:14px;font-weight:600;color:var(--brand)}

/* contact */
.contact{top:3155px;height:415px;background:linear-gradient(135deg,#6b4c38,#5b3f2e 60%,#6f503b)}
.contact .section-title{color:var(--white)}
.field{width:440px;height:35px;border:1px solid #d9c6b8;background:var(--field);color:var(--white);font-size:13px;padding:8px 18px}
.field-message{left:628px;top:128px;height:162px}
.submit{left:130px;top:315px;width:160px;height:50px;line-height:46px;font-size:22px;font-weight:400;border:2px solid #c46a4a}

/* footer */
.site-footer{top:3570px;height:180px;background:var(--light);text-align:center}
.social{left:512px;top:35px;display:flex;gap:10px}
.social span{width:16px;height:16px;border-radius:50%}
.footer-nav{width:1200px;top:88px;display:flex;justify-content:center;gap:45px;font-size:12px;color:#444}
.copyright{width:1200px;top:128px;font-size:11px;color:#666}
</style>
</head>
<body>

<header class="site-header">
  <div class="brand abs"><span class="brand-dot"></span>CodeHarbor</div>
  <nav class="main-nav abs">
    <span class="active">HOME</span><span>ABOUT US</span><span>SERVICES</span><span>OUR WORKS</span><span>NEWS</span><span>CONTACT US</span>
  </nav>
</header>

<section class="hero" role="img" aria-label="Hero photograph of software engineers working at screens full of code">
  <svg class="hero-arrow abs" style="left:22px" viewBox="0 0 60 60"><circle cx="30" cy="30" r="27" fill="none" stroke="#fff" stroke-width="3"/><path d="M36 17 L20 30 L36 43 Z" fill="#fff"/></svg>
  <svg class="hero-arrow abs" style="left:1118px" viewBox="0 0 60 60"><circle cx="30" cy="30" r="27" fill="none" stroke="#fff" stroke-width="3"/><path d="M24 17 L40 30 L24 43 Z" fill="#fff"/></svg>
  <div class="hero-caption abs">Neque porro quisquam est qui dolorem ipsum<br>quia dolor sit amet, consectetur, adipisci velit</div>
  <span class="btn hero-btn abs">LEARN MORE</span>
  <svg class="diamond abs" style="top:490px;opacity:.35" viewBox="0 0 80 80"><rect x="16" y="16" width="48" height="48" transform="rotate(45 40 40)" fill="none" stroke="#fff" stroke-width="3"/><path d="M26 34 L40 48 L54 34" fill="none" stroke="#fff" stroke-width="3"/></svg>
</section>

<section class="about">
  <h2 class="section-title abs" style="top:25px">~ ABOUT US ~</h2>
  <div class="about-col abs" style="left:137px;top:90px"><h3>Our Mission</h3><p>"At vero eos et accusamus et iusto odio dignissimos ducimus qui blanditiis praesentium voluptatum deleniti atque corrupti quos dolores et quas molestias."</p></div>
  <div class="about-col abs" style="left:455px;top:90px"><h3>Our Vission</h3><p>"At vero eos et accusamus et iusto odio dignissimos ducimus qui blanditiis praesentium voluptatum deleniti atque corrupti quos dolores et quas molestias."</p></div>
  <div class="about-col abs" style="left:790px;top:90px"><h3>What We Do?</h3><p>"At vero eos et accusamus et iusto odio dignissimos ducimus qui blanditiis praesentium voluptatum deleniti atque corrupti quos dolores et quas molestias."</p></div>
  <div class="team-title abs">~ Our Team ~</div>
  <div class="member abs" style="left:130px;top:290px"><div class="member-photo" role="img" aria-label="Team member portrait"></div><div class="member-info"><strong>Colin Marsh</strong>Email: colin@codeharbor.test<br>Phone: +00 000 000 000<br>Aenean in magna aliquet maecenas<br>ligula urna placerat in lect.</div></div>
  <div class="member abs" style="left:458px;top:290px"><div class="member-photo" role="img" aria-label="Team member portrait"></div><div class="member-info"><strong>Colin Marsh</strong>Email: colin@codeharbor.test<br>Phone: +00 000 000 000<br>Aenean in magna aliquet maecenas<br>ligula urna placerat in lect.</div></div>
  <div class="member abs" style="left:783px;top:290px"><div class="member-photo" role="img" aria-label="Team member portrait"></div><div class="member-info"><strong>Colin Marsh</strong>Email: colin@codeharbor.test<br>Phone: +00 000 000 000<br>Aenean in magna aliquet maecenas<br>ligula urna placerat in lect.</div></div>
  <svg class="diamond abs" style="top:445px" viewBox="0 0 80 80"><rect x="16" y="16" width="48" height="48" transform="rotate(45 40 40)" fill="#fff" stroke="var(--diamond)" stroke-width="3"/><path d="M26 34 L40 48 L54 34" fill="none" stroke="var(--diamond)" stroke-width="3"/></svg>
</section>

<section class="services">
  <h2 class="section-title abs" style="top:40px">~ OUR SERVICES ~</h2>
  <!-- row 1: core selling points -->
  <div class="service abs" style="left:130px;top:135px"><span class="service-icon" style="background:#f4b400"><svg width="30" height="30" viewBox="0 0 30 30"><path d="M10 8 L3 15 L10 22 M20 8 L27 15 L20 22" fill="none" stroke="#fff" stroke-width="3"/></svg></span><div><h4>Custom Software Development</h4><p>Tailored code built around your<br>own business processes.</p></div></div>
  <div class="service abs" style="left:470px;top:135px"><span class="service-icon" style="background:#e8542a"><svg width="30" height="30" viewBox="0 0 30 30"><rect x="4" y="6" width="12" height="4" fill="#fff"/><rect x="9" y="13" width="14" height="4" fill="#fff"/><rect x="14" y="20" width="12" height="4" fill="#fff"/></svg></span><div><h4>Project Management</h4><p>Clear plans, milestones and<br>reporting from start to launch.</p></div></div>
  <div class="service abs" style="left:795px;top:135px"><span class="service-icon" style="background:#3b8dbd"><svg width="30" height="30" viewBox="0 0 30 30"><circle cx="15" cy="15" r="5" fill="none" stroke="#fff" stroke-width="3"/><path d="M15 3v5M15 22v5M3 15h5M22 15h5M6.5 6.5l3.5 3.5M20 20l3.5 3.5M6.5 23.5l3.5-3.5M20 10l3.5-3.5" stroke="#fff" stroke-width="3"/></svg></span><div><h4>Industry Services</h4><p>Solutions shaped for your sector<br>and its specific standards.</p></div></div>
  <!-- row 2 -->
  <div class="service abs" style="left:130px;top:245px"><span class="service-icon" style="background:#5ab04a"><svg width="30" height="30" viewBox="0 0 30 30"><rect x="3" y="5" width="24" height="17" rx="2" fill="none" stroke="#fff" stroke-width="3"/><path d="M10 26h10" stroke="#fff" stroke-width="3"/></svg></span><div><h4>Web &amp; Desktop Applications</h4><p>Responsive interfaces for every<br>screen your users work on.</p></div></div>
  <div class="service abs" style="left:470px;top:245px"><span class="service-icon" style="background:#f6b800"><svg width="30" height="30" viewBox="0 0 30 30"><rect x="6" y="5" width="18" height="21" rx="2" fill="none" stroke="#fff" stroke-width="3"/><path d="M10 13l3 3 6-6" fill="none" stroke="#fff" stroke-width="3"/></svg></span><div><h4>Agile Sprint Planning</h4><p>Short cycles with working builds<br>delivered every two weeks.</p></div></div>
  <div class="service abs" style="left:795px;top:245px"><span class="service-icon" style="background:#d6234a"><svg width="30" height="30" viewBox="0 0 30 30"><ellipse cx="15" cy="8" rx="9" ry="3.5" fill="none" stroke="#fff" stroke-width="3"/><path d="M6 8v14c0 2 4 3.5 9 3.5s9-1.5 9-3.5V8" fill="none" stroke="#fff" stroke-width="3"/></svg></span><div><h4>Legacy System Upgrades</h4><p>Modernise older platforms while<br>keeping your data safe.</p></div></div>
  <!-- row 3 -->
  <div class="service abs" style="left:130px;top:355px"><span class="service-icon" style="background:#d81b50"><svg width="30" height="30" viewBox="0 0 30 30"><circle cx="8" cy="15" r="4" fill="#fff"/><circle cx="22" cy="8" r="4" fill="#fff"/><circle cx="22" cy="22" r="4" fill="#fff"/><path d="M8 15L22 8M8 15l14 7" stroke="#fff" stroke-width="2.5"/></svg></span><div><h4>API &amp; Systems Integration</h4><p>Connect your tools so data<br>flows where it is needed.</p></div></div>
  <div class="service abs" style="left:470px;top:355px"><span class="service-icon" style="background:#3e8fc2"><svg width="30" height="30" viewBox="0 0 30 30"><path d="M4 26V4M4 26h22" stroke="#fff" stroke-width="3" fill="none"/><path d="M8 20l6-6 4 4 7-8" stroke="#fff" stroke-width="3" fill="none"/></svg></span><div><h4>Delivery &amp; QA Tracking</h4><p>Testing and progress reports<br>kept open to your team.</p></div></div>
  <div class="service abs" style="left:795px;top:355px"><span class="service-icon" style="background:#4caf50"><svg width="30" height="30" viewBox="0 0 30 30"><path d="M9 22a6 6 0 0 1 0-12 8 8 0 0 1 15 2 5 5 0 0 1-1 10z" fill="none" stroke="#fff" stroke-width="3"/></svg></span><div><h4>Cloud &amp; DevOps Support</h4><p>Hosting, deployment pipelines<br>and ongoing monitoring.</p></div></div>
  <svg class="diamond abs" style="top:465px" viewBox="0 0 80 80"><rect x="16" y="16" width="48" height="48" transform="rotate(45 40 40)" fill="none" stroke="#fff" stroke-width="3"/><path d="M26 34 L40 48 L54 34" fill="none" stroke="#fff" stroke-width="3"/></svg>
</section>

<section class="works">
  <h2 class="section-title abs" style="top:45px">~ Our Works~</h2>
  <div class="work abs" style="left:130px;top:115px"><div class="work-image" role="img" aria-label="Project photo: developers reviewing code on a monitor" style="background:linear-gradient(135deg,#2d3b4e,#5c7a99)"></div><h4>Neque porro quisquam est qui</h4><p>olor sit amet, consectetur, adipisci velit.</p></div>
  <div class="work abs" style="left:455px;top:115px"><div class="work-image" role="img" aria-label="Project photo: team planning a software architecture at a whiteboard" style="background:linear-gradient(135deg,#dfe6ea,#a9b4bd)"></div><h4>Neque porro quisquam est qui</h4><p>olor sit amet, consectetur, adipisci velit.</p></div>
  <div class="work abs" style="left:783px;top:115px"><div class="work-image" role="img" aria-label="Project photo: dashboard application on a laptop" style="background:linear-gradient(135deg,#7d8590,#d1d5da)"></div><h4>Neque porro quisquam est qui</h4><p>olor sit amet, consectetur, adipisci velit.</p></div>
  <div class="work abs" style="left:130px;top:427px"><div class="work-image" role="img" aria-label="Project photo: mobile app screens" style="background:linear-gradient(135deg,#eef0f2,#9ea4aa)"></div><h4>Neque porro quisquam est qui</h4><p>olor sit amet, consectetur, adipisci velit.</p></div>
  <div class="work abs" style="left:455px;top:427px"><div class="work-image" role="img" aria-label="Project photo: engineer at a multi-screen workstation" style="background:linear-gradient(135deg,#3a3f47,#7c8a99)"></div><h4>Neque porro quisquam est qui</h4><p>olor sit amet, consectetur, adipisci velit.</p></div>
  <div class="work abs" style="left:783px;top:427px"><div class="work-image" role="img" aria-label="Project photo: server room for a cloud deployment" style="background:linear-gradient(135deg,#8fa0b5,#1f3050)"></div><h4>Neque porro quisquam est qui</h4><p>olor sit amet, consectetur, adipisci velit.</p></div>
  <svg class="diamond abs" style="top:755px" viewBox="0 0 80 80"><rect x="16" y="16" width="48" height="48" transform="rotate(45 40 40)" fill="#fff" stroke="var(--diamond)" stroke-width="3"/><path d="M26 34 L40 48 L54 34" fill="none" stroke="var(--diamond)" stroke-width="3"/></svg>
</section>

<section class="jobs" role="img" aria-label="Background photograph of a modern software office">
  <h2 class="abs">OUR JOB POSTINGS</h2>
  <p class="abs">Neque porro quisquam est qui dolorem ipsum quia<br>dolor sit amet, consectetur, adipisci velit.</p>
  <span class="btn jobs-btn abs">View More Here</span>
</section>

<section class="tweet">
  <span class="tweet-mark abs"></span>
  <span class="tweet-quote abs">“</span>
  <p class="tweet-text abs">Hi, we certainly don't Neque porro quisquam est qui dolorem ipsum quia dolor sit amet, consectetur, adipisci velit.want to give t Thank fhdfNeque porro quisquam est qui dolorem ipsum quia dolor sit amet, consectetur, adipisci velit.yhyuu fo</p>
  <div class="tweet-time abs">2 days ago</div>
  <svg class="diamond abs" style="top:205px" viewBox="0 0 80 80"><rect x="16" y="16" width="48" height="48" transform="rotate(45 40 40)" fill="#fff" stroke="var(--diamond)" stroke-width="3"/><path d="M26 34 L40 48 L54 34" fill="none" stroke="var(--diamond)" stroke-width="3"/></svg>
</section>

<section class="contact" role="img" aria-label="Street map background showing the office location">
  <h2 class="section-title abs" style="top:40px">~ CONTACT US ~</h2>
  <div class="field abs" style="left:130px;top:128px">Name</div>
  <div class="field abs" style="left:130px;top:186px">Email</div>
  <div class="field abs" style="left:130px;top:243px">Ph:No</div>
  <div class="field field-message abs">Message</div>
  <svg class="abs" style="left:688px;top:215px" width="22" height="30" viewBox="0 0 22 30"><path d="M11 29 C4 18 1 14 1 10 a10 10 0 0 1 20 0 c0 4-3 8-10 19z" fill="#c0392b"/><circle cx="11" cy="10" r="4" fill="#fff"/></svg>
  <span class="btn submit abs">SUBMIT</span>
</section>

<footer class="site-footer">
  <div class="social abs">
    <span style="background:#3b5998" aria-label="Social link"></span>
    <span style="background:#2fb6e8" aria-label="Social link"></span>
    <span style="background:#f39c12" aria-label="Social link"></span>
    <span style="background:#dd4b39" aria-label="Social link"></span>
    <span style="background:#0e76a8" aria-label="Social link"></span>
    <span style="background:#ea4c89" aria-label="Social link"></span>
  </div>
  <nav class="footer-nav abs"><span>HOME</span><span>ABOUT US</span><span>SERVICES</span><span>OUR WORKS</span><span>NEWS</span><span>CONTACT US</span></nav>
  <p class="copyright abs">All 2014 Copyrights are reserved</p>
</footer>

</body>
</html>
```